Business Card Design Project

We have recently completed CraftHive projects for a new logo and wesbite.
We now require new business cards.
We hand out very little printed material to clients as all information is online. When we do hand out something, like a business card, we want it to have real impact and make a statement about the quality and professionalism of our company.
We have an idea of what we want our card to look like but we want a designer to make sure they have impact and look great.
Our requirements are…
Size: 85mm X 55mm - Landscape
Front of card: Logo plus the following contact information.
Tobias Marsh
Operations Manager
Phone +44(0) 1632 xxx xxx
Mobile +44(0) 7700 xxx xxx
Email tobym@korvexsys.example
Address 19 Pellow Row, Aberdeen AB12 3QJ
Website www.korvexsys.example
How you layout the front of the card is up to you, we would like to see some different ideas. Attached are two versions of our logo that may be used.
Back of card: We would like this to be simple but again have impact. Our current thought is to have the logo or just the large W design from the logo in white against a dark background, perhaps made up from the dark green in the logo.
The logos are attached so you can see the colours in them but the dark ones are..
Dark Blue = C:88, M:55, Y:44, K:28
Dark Green = C:87, M:53, Y:50, K:50
We sometimes also use a bright orange as an accent or highlight colour…
Orange: = C:0, M:39, Y:94, K:0

```html
<!DOCTYPE html>
<html lang="en">
<head>
<meta charset="utf-8">
<title>Korvex Systems – Business Card</title>
<link href="https://fonts.googleapis.com/css2?family=Lato:wght@400;700&display=swap" rel="stylesheet">
<style>
  :root {
    --page-bg: #e4e8ea;
    --card-white: #ffffff;
    --brand-teal: #2f5b69;
    --brand-teal-deep: #244a57;
    --brand-teal-light: #4f8190;
    --text-grey: #3f4447;
    --text-soft: #555b5f;
    --on-dark: #ffffff;
  }
  * { box-sizing: border-box; margin: 0; padding: 0; }
  html, body {
    width: 1200px; height: 960px; overflow: hidden;
    background: var(--page-bg);
    font-family: "Lato", Arial, sans-serif;
  }
  .sheet {
    width: 1200px; height: 960px;
    display: flex; flex-direction: column;
    align-items: center; justify-content: center; gap: 56px;
  }
  .card {
    position: relative;
    width: 620px; height: 401px;
    box-shadow: 0 10px 28px rgba(30, 50, 60, 0.18);
    overflow: hidden;
  }

  /* Front */
  .card-front { background: var(--card-white); }
  .brand {
    position: absolute; left: 46px; top: 128px;
    display: flex; align-items: center; gap: 12px;
  }
  .brand-square {
    width: 22px; height: 22px; flex: none; background: var(--brand-teal);
  }
  .brand-name {
    font-weight: 700; font-size: 34px; letter-spacing: 0.5px;
    color: var(--brand-teal); line-height: 1.05;
  }
  .brand-name span { display: block; }
  .person {
    position: absolute; left: 360px; top: 160px;
    color: var(--text-grey);
  }
  .person-name {
    font-size: 22px; font-weight: 400; letter-spacing: 0.6px; text-transform: uppercase;
  }
  .person-role {
    margin-top: 6px; font-size: 14px; letter-spacing: 0.8px; color: var(--text-soft);
  }
  .contact-list {
    position: absolute; left: 360px; top: 300px;
    list-style: none; font-size: 14px; color: var(--text-grey); line-height: 1;
  }
  .contact-list li { display: flex; align-items: center; gap: 10px; margin-bottom: 7px; white-space: nowrap; }
  .contact-icon { width: 13px; height: 13px; flex: none; }
  .contact-icon path, .contact-icon rect { fill: none; stroke: var(--text-grey); stroke-width: 1.3; }
  .location {
    position: absolute; left: 46px; top: 318px;
    font-size: 16px; color: var(--text-grey);
  }
  .location .website {
    display: block; margin-top: 10px;
    font-weight: 700; color: var(--brand-teal-deep);
  }

  /* Back */
  .card-back {
    background: radial-gradient(ellipse at 35% 20%, var(--brand-teal-light) 0%, var(--brand-teal) 55%, var(--brand-teal-deep) 100%);
  }
  .card-back .brand { left: 52px; top: 206px; }
  .card-back .brand-square { background: var(--on-dark); }
  .card-back .brand-name { color: var(--on-dark); font-size: 44px; }
</style>
</head>
<body>
<main class="sheet">
  <section class="card card-front" aria-label="Card front">
    <div class="brand">
      <span class="brand-square"></span>
      <span class="brand-name"><span>KORVEX</span><span>SYSTEMS</span></span>
    </div>
    <div class="person">
      <p class="person-name">Tobias Marsh</p>
      <p class="person-role">Operations Manager</p>
    </div>
    <ul class="contact-list">
      <li>
        <svg class="contact-icon" viewBox="0 0 13 13" aria-hidden="true"><rect x="2" y="1" width="9" height="11" rx="1"/><path d="M4 4h5M4 7h5"/></svg>
        +44(0) 1632 xxx xxx
      </li>
      <li>
        <svg class="contact-icon" viewBox="0 0 13 13" aria-hidden="true"><rect x="3.5" y="1" width="6" height="11" rx="1"/><path d="M5 10h3"/></svg>
        +44(0) 7700 xxx xxx
      </li>
      <li>
        <svg class="contact-icon" viewBox="0 0 13 13" aria-hidden="true"><rect x="1" y="3" width="11" height="7"/><path d="M1 3l5.5 4L12 3"/></svg>
        tobym@korvexsys.example
      </li>
    </ul>
    <p class="location">
      19 Pellow Row, Aberdeen AB12 3QJ
      <span class="website">www.korvexsys.example</span>
    </p>
  </section>

  <section class="card card-back" aria-label="Card back">
    <div class="brand">
      <span class="brand-square"></span>
      <span class="brand-name"><span>KORVEX</span><span>SYSTEMS</span></span>
    </div>
  </section>
</main>
</body>
</html>
```